Menu Design Project

This is a sushi menu. We need to polish the menu. You can re-size logo and add color and graphic to make inviting. Please feel free to make any recommendations.

Target Market(s)

Upscale crowd

```html
<!DOCTYPE html>
<html lang="en">
<head>
<meta charset="utf-8">
<title>Kaiyo Sushi Bar — Menu</title>
<link rel="stylesheet" href="https://fonts.googleapis.com/css2?family=Roboto+Condensed:wght@300;400;700&display=swap">
<style>
:root{
  --paper:#ffffff;
  --ink:#111111;
  --heading:#8b5a78;
  --accent:#d4141b;
  --muted:#b9cfd0;
  --texture-light:#f1f1f1;
  --texture-dark:#dcdcdc;
}
*{margin:0;padding:0;box-sizing:border-box}
html,body{width:1200px;height:800px;overflow:hidden;background:var(--paper)}
body{font-family:"Roboto Condensed",Arial,sans-serif;color:var(--ink)}
.menu{position:relative;width:1296px;height:864px;transform:scale(0.925926);transform-origin:0 0;background:var(--paper)}
.texture{position:absolute;top:0;height:864px;background:linear-gradient(180deg,var(--texture-light) 0%,var(--texture-light) 85%,var(--texture-dark) 100%)}
.texture--left{left:0;width:103px}
.texture--right{left:1120px;width:176px}
.brand{position:absolute;display:flex;flex-direction:column;align-items:center;justify-content:center;gap:8px;background:var(--paper)}
.brand--left{left:0;top:312px;width:130px;height:196px}
.brand--right{left:1140px;top:672px;width:130px;height:176px;background:transparent}
.brand__dot{width:58px;height:58px;border-radius:50%;background:var(--accent)}
.brand__name{font-weight:700;font-size:20px;line-height:1.05;text-align:center;letter-spacing:1px;text-transform:uppercase;color:var(--ink)}
.heading{position:absolute;font-weight:300;font-size:23px;letter-spacing:2px;color:var(--heading);transform:translateX(-50%);white-space:nowrap}
.list{position:absolute;left:0;width:1296px}
.row{position:relative;height:18px;font-size:12.5px;letter-spacing:.5px;line-height:18px;white-space:nowrap}
.row span{position:absolute;top:0}
.name{font-weight:700;text-align:right}
.desc{font-weight:400}
.price{font-weight:700}
/* left columns */
.col-a .name{left:0;width:255px}
.col-a .desc{left:291px}
.col-a .price{left:596px}
/* right columns */
.col-b .name{left:0;width:773px}
.col-b .desc{left:803px}
.col-b .price{left:1090px}
.col-b .price-mid{left:803px;font-weight:700}
.col-b .name-right{left:0;width:1066px;font-weight:700;text-align:right}
.col-b .sub-name{left:819px;font-weight:700}
/* sidebar */
.col-c .name{left:0;width:1244px}
.col-c .price{left:1262px}
.note{position:absolute;left:0;width:1244px;text-align:right;font-size:11px;font-style:italic;color:var(--muted)}
.row--tall{height:30px}
.desc--wrap{line-height:12px;top:2px!important}
</style>
</head>
<body>
<main class="menu">
  <div class="texture texture--left" role="img" aria-label="fine diagonal line texture"></div>
  <div class="texture texture--right" role="img" aria-label="fine diagonal line texture"></div>

  <div class="brand brand--left"><div class="brand__dot"></div><div class="brand__name">Kaiyo<br>Sushi Bar</div></div>
  <div class="brand brand--right"><div class="brand__dot"></div><div class="brand__name">Kaiyo<br>Sushi Bar</div></div>

  <!-- appetizers -->
  <h2 class="heading" style="left:373px;top:10px">appetizers</h2>
  <section class="list col-a" style="top:47px">
    <div class="row"><span class="name">edamame</span><span class="desc">soybeans &amp; seasalt</span><span class="price">3.5</span></div>
    <div class="row"><span class="name">spicy garlic edamame</span><span class="desc">soybeans, seasalt &amp; spicy garlic</span><span class="price">4.5</span></div>
    <div class="row"><span class="name">sautéed asparagus</span><span class="desc">asparagus &amp; teriyaki sauce</span><span class="price">4.5</span></div>
    <div class="row"><span class="name">sautéed shiitake</span><span class="desc">mushrooms, onions &amp; cream sauce</span><span class="price">5</span></div>
    <div class="row"><span class="name">age dashi tofu</span><span class="desc">tofu, sweet dashi soy sauce &amp; bonito flakes</span><span class="price">5</span></div>
    <div class="row"><span class="name">yakitori</span><span class="desc">teriyaki chicken &amp; vegetables served on skewers</span><span class="price">6</span></div>
    <div class="row"><span class="name">gyoza</span><span class="desc">beef &amp; vegetable dumplings</span><span class="price">5.5</span></div>
    <div class="row"><span class="name">shumai</span><span class="desc">shrimp dumplings &amp; ponzu sauce</span><span class="price">5.5</span></div>
    <div class="row"><span class="name">soft shell crab</span><span class="desc">fried soft-shell crab &amp; ponzu sauce</span><span class="price">9</span></div>
    <div class="row"><span class="name">tatsuta-age</span><span class="desc">panko breaded chicke, garlic &amp; tempura sauce</span><span class="price">6</span></div>
    <div class="row"><span class="name">tako su</span><span class="desc">octupus marinated in citrus sauce</span><span class="price">7</span></div>
    <div class="row"><span class="name">calimari rings</span><span class="desc">fried calamari &amp; tempura sauce</span><span class="price">8</span></div>
    <div class="row"><span class="name">grilled calamari</span><span class="desc">marinated in lemon teriyaki sauce, garlic &amp; ginger</span><span class="price">8</span></div>
    <div class="row"><span class="name">hamachi kama</span><span class="desc">yellowtail collar &amp; ponzu sauce</span><span class="price">8</span></div>
    <div class="row"><span class="name">mixed tempura</span><span class="desc">tempura shrimp &amp; vegetables</span><span class="price">7</span></div>
    <div class="row"><span class="name">vegetable tempura</span><span class="desc">tempura vegetables</span><span class="price">6</span></div>
    <div class="row"><span class="name">chicken katsu</span><span class="desc">breaded chicken skewers &amp; japanese barbecue sauce</span><span class="price">5.5</span></div>
  </section>

  <!-- entrees -->
  <h2 class="heading" style="left:868px;top:10px">entrees</h2>
  <section class="list col-b" style="top:46px">
    <div class="row"><span class="name">edamame</span><span class="desc">soybeans &amp; seasalt</span><span class="price">3.5</span></div>
    <div class="row"><span class="name">spicy garlic edamame</span><span class="desc">soybeans, seasalt &amp; spicy garlic</span><span class="price">4.5</span></div>
    <div class="row"><span class="name">sautéed asparagus</span><span class="desc">asparagus &amp; teriyaki sauce</span><span class="price">4.5</span></div>
    <div class="row"><span class="name">sautéed shiitake</span><span class="desc">mushrooms, onions &amp; cream sauce</span><span class="price">5</span></div>
    <div class="row"><span class="name">age dashi tofu</span><span class="desc">tofu, sweet dashi soy sauce &amp; bonito flakes</span><span class="price">5</span></div>
    <div class="row"><span class="name">yakitori</span><span class="desc">teriyaki chicken &amp; vegetables served on skewers</span><span class="price">6</span></div>
    <div class="row"><span class="name">gyoza</span><span class="desc">beef &amp; vegetable dumplings</span><span class="price">5.5</span></div>
    <div class="row"><span class="name">shumai</span><span class="desc">shrimp dumplings &amp; ponzu sauce</span><span class="price">5.5</span></div>
    <div class="row"><span class="name">soft shell crab</span><span class="desc">fried soft-shell crab &amp; ponzu sauce</span><span class="price">9</span></div>
    <div class="row"><span class="name">tatsuta-age</span><span class="price-mid">6</span><span class="name-right">tatsuta-age</span><span class="price">6</span></div>
    <div class="row"><span class="name">tako su</span><span class="price-mid">7</span><span class="name-right">tako su</span><span class="price">7</span></div>
    <div class="row"><span class="name">calimari rings</span><span class="price-mid">8</span><span class="name-right">calimari rings</span><span class="price">8</span></div>
    <div class="row"><span class="name">grilled calamari</span><span class="price-mid">8</span><span class="name-right">grilled calamari</span><span class="price">8</span></div>
    <div class="row"><span class="name">hamachi kama</span><span class="price-mid">8</span><span class="name-right">hamachi kama</span><span class="price">8</span></div>
    <div class="row"><span class="name">mixed tempura</span><span class="price-mid">7</span><span class="name-right">mixed tempura</span><span class="price">7</span></div>
    <div class="row"><span class="name">vegetable tempura</span><span class="price-mid">6</span><span class="name-right">vegetable tempura</span><span class="price">6</span></div>
    <div class="row"><span class="name">chicken katsu</span><span class="price-mid">5.5</span><span class="name-right">chicken katsu</span><span class="price">5.5</span></div>
  </section>

  <!-- noodles -->
  <h2 class="heading" style="left:358px;top:367px">noodles</h2>
  <section class="list col-a" style="top:405px">
    <div class="row"><span class="name">edamame</span><span class="desc">soybeans &amp; seasalt</span><span class="price">3.5</span></div>
    <div class="row"><span class="name">spicy garlic edamame</span><span class="desc">soybeans, seasalt &amp; spicy garlic</span><span class="price">4.5</span></div>
    <div class="row"><span class="name">sautéed asparagus</span><span class="desc">asparagus &amp; teriyaki sauce</span><span class="price">4.5</span></div>
    <div class="row"><span class="name">sautéed shiitake</span><span class="desc">mushrooms, onions &amp; cream sauce</span><span class="price">5</span></div>
    <div class="row"><span class="name">age dashi tofu</span><span class="desc">tofu, sweet dashi soy sauce &amp; bonito flakes</span><span class="price">5</span></div>
    <div class="row"><span class="name">yakitori</span><span class="desc">teriyaki chicken &amp; vegetables served on skewers</span><span class="price">6</span></div>
    <div class="row"><span class="name">gyoza</span><span class="desc">beef &amp; vegetable dumplings</span><span class="price">5.5</span></div>
    <div class="row"><span class="name">shumai</span><span class="desc">shrimp dumplings &amp; ponzu sauce</span><span class="price">5.5</span></div>
    <div class="row"><span class="name">soft shell crab</span><span class="desc">fried soft-shell crab &amp; ponzu sauce</span><span class="price">9</span></div>
    <div class="row"><span class="name">tatsuta-age</span><span class="desc">panko breaded chicke, garlic &amp; tempura sauce</span><span class="price">6</span></div>
    <div class="row"><span class="name">tako su</span><span class="desc">octupus marinated in citrus sauce</span><span class="price">7</span></div>
    <div class="row"><span class="name">calimari rings</span><span class="price">8</span></div>
  </section>

  <!-- soups -->
  <h2 class="heading" style="left:348px;top:623px">soups</h2>
  <section class="list col-a" style="top:659px">
    <div class="row"><span class="name">edamame</span><span class="desc">soybeans &amp; seasalt</span><span class="price">3.5</span></div>
    <div class="row"><span class="name">spicy garlic edamame</span><span class="desc">soybeans, seasalt &amp; spicy garlic</span><span class="price">4.5</span></div>
    <div class="row"><span class="name">sautéed asparagus</span><span class="desc">asparagus &amp; teriyaki sauce</span><span class="price">4.5</span></div>
    <div class="row"><span class="name">sautéed shiitake</span><span class="desc">mushrooms, onions &amp; cream sauce</span><span class="price">5</span></div>
  </section>

  <!-- salads -->
  <h2 class="heading" style="left:620px;top:744px">salads</h2>
  <section class="list col-a" style="top:780px">
    <div class="row"><span class="name">edamame</span><span class="desc">soybeans &amp; seasalt</span><span class="price">3.5</span></div>
    <div class="row"><span class="name">spicy garlic edamame</span><span class="desc">soybeans, seasalt &amp; spicy garlic</span><span class="price">4.5</span></div>
    <div class="row"><span class="name">sautéed asparagus</span><span class="desc">asparagus &amp; teriyaki sauce</span><span class="price">4.5</span></div>
    <div class="row"><span class="name">sautéed shiitake</span><span class="desc">mushrooms, onions &amp; cream sauce</span><span class="price">5</span></div>
  </section>
  <section class="list col-b" style="top:780px">
    <div class="row"><span class="name">edamame</span><span class="desc">soybeans &amp; seasalt</span><span class="price">3.5</span></div>
    <div class="row"><span class="name">spicy garlic edamame</span><span class="desc">soybeans, seasalt &amp; spicy garlic</span><span class="price">4.5</span></div>
    <div class="row"><span class="name">sautéed asparagus</span><span class="desc">asparagus &amp; teriyaki sauce</span><span class="price">4.5</span></div>
    <div class="row"><span class="name">sautéed shiitake</span><span class="desc">mushrooms, onions &amp; cream sauce</span><span class="price">5</span></div>
  </section>

  <!-- specials -->
  <h2 class="heading" style="left:873px;top:367px">specials</h2>
  <section class="list col-b" style="top:405px">
    <div class="row" style="height:27px"><span class="name">bento box</span><span class="desc">soybeans &amp; seasalt, soybeans, seasalt &amp; spicy garlic</span></div>
    <div class="row"><span class="price-mid">6</span><span class="sub-name">beef teriyaki</span><span class="name-right">tatsuta-age</span><span class="price">6</span></div>
    <div class="row"><span class="price-mid">7</span><span class="sub-name">chicken teriyaki</span><span class="name-right">tako su</span><span class="price">7</span></div>
    <div class="row" style="height:33px"><span class="price-mid">8</span><span class="sub-name">salmon teriyaki</span><span class="name-right">calimari rings</span><span class="price">8</span></div>
    <div class="row row--tall"><span class="name">kaiyo box</span><span class="desc desc--wrap">soybeans &amp; seasalt, soybeans, seasalt &amp; spicy garlic<br>teriyaki chicken (6), fishfood, sushi, etc.</span><span class="price">3.5</span></div>
    <div class="row"><span class="name">edamame</span><span class="desc">soybeans &amp; seasalt</span><span class="price" style="top:5px">4.5</span></div>
    <div class="row"><span class="name">spicy garlic edamame</span><span class="desc">soybeans, seasalt &amp; spicy garlic</span><span class="price" style="top:5px">5</span></div>
    <div class="row"><span class="name">sautéed asparagus</span><span class="desc">asparagus &amp; teriyaki sauce</span><span class="price" style="top:5px">5</span></div>
    <div class="row"><span class="name">sautéed shiitake</span><span class="desc">mushrooms, onions &amp; cream sauce</span><span class="price" style="top:5px">6</span></div>
    <div class="row" style="height:32px"><span class="name">age dashi tofu</span><span class="desc">tofu, sweet dashi soy sauce &amp; bonito flakes</span><span class="price" style="top:5px">5.5</span></div>
    <div class="row"><span class="name" style="top:4px">tatsuta-age</span><span class="price-mid" style="top:6px">6</span><span class="name-right">tatsuta-age</span><span class="price">6</span></div>
    <div class="row"><span class="name" style="top:4px">tako su</span><span class="price-mid" style="top:6px">7</span><span class="name-right">tako su</span><span class="price">7</span></div>
    <div class="row"><span class="name" style="top:4px">calimari rings</span><span class="price-mid" style="top:6px">8</span><span class="name-right">calimari rings</span><span class="price">8</span></div>
  </section>

  <!-- drinks -->
  <h2 class="heading" style="left:1216px;top:10px">drinks</h2>
  <section class="list col-c" style="top:48px">
    <div class="row"><span class="name">cola</span><span class="price">3.5</span></div>
    <div class="row"><span class="name">diet cola</span><span class="price">4.5</span></div>
    <div class="row"><span class="name">lemon-lime</span><span class="price">4.5</span></div>
    <div class="row"><span class="name">orange soda</span><span class="price">5</span></div>
    <div class="row"><span class="name">lemonade</span><span class="price">5</span></div>
    <div class="row"><span class="name">orange &amp; apple juice</span><span class="price">5</span></div>
    <div class="row"><span class="note">no refills on juice</span></div>
    <div class="row"><span class="name">iced tea</span><span class="price">6</span></div>
    <div class="row"><span class="name">hot japanese green tea</span><span class="price">5.5</span></div>
  </section>

  <!-- sides -->
  <h2 class="heading" style="left:1216px;top:249px">sides</h2>
  <section class="list col-c" style="top:286px">
    <div class="row"><span class="name">steamed rice</span><span class="price">3.5</span></div>
    <div class="row"><span class="name">brown rice</span><span class="price">4.5</span></div>
    <div class="row"><span class="name">sushi rice</span><span class="price">4.5</span></div>
    <div class="row"><span class="name">avocado</span><span class="price">5</span></div>
    <div class="row"><span class="name">tofu</span><span class="price">5</span></div>
    <div class="row"><span class="name">shrimp tempura (1pc.)</span><span class="price">5</span></div>
    <div class="row"><span class="name">teriyaki sauce</span><span class="price">6</span></div>
    <div class="row"><span class="name">ginger dressing</span><span class="price">5.5</span></div>
  </section>

  <!-- desert -->
  <h2 class="heading" style="left:1216px;top:473px">desert</h2>
  <section class="list col-c" style="top:510px">
    <div class="row"><span class="name">steamed rice</span><span class="price">3.5</span></div>
    <div class="row"><span class="name">brown rice</span><span class="price">4.5</span></div>
    <div class="row"><span class="name">sushi rice</span><span class="price">4.5</span></div>
  </section>
</main>
</body>
</html>
```